Gourmet food company looking for a dazzling label for their premuim vinagrette dressings

Need a food label that will dazzle our customer and prove what a premium product we have. We make high end gourmet dressing for vegetables, fruit, meat, poultry and fish.

Our label will fit on a 250 mil Tolvenna Square bottle. Labels should be a 4x5 or even 5x5 depending on the design. Nutritionals, bar codes and company blurb will be supplied later. We really want to test you all's talent on this one and are very excited to see your renderings!

Our dressings are Champagne Pear Vinaigrette, White Balsmic Vinaigrette, Mojito Lime Vinaigrette, Creamy-Avacado Lime Vinaigrette, and Asian Sesame Vinaigrette. I hope these names will help you envision our product and kinda what we are looking for.

Thank you all so far for your renderings.I really don't want pictures if that helps. Our logo can be smaller and/or the name of the product bigger. Perhaps we can even redesign Lumora and remove the leaf as I don't really care for what I see yet.So good luck and thanks Added Friday, August 19, 2016

I am still looking for that clean - elegant design for our product as our product is just that. If you look on the internet at vinegars and oils you will see many designs that are simple yet elegant. Creative lettering, bordering, color (can be black and white) and size will help accomplish this. So I invite you to use all your creativity and help me find just what we need.Many thanks Added Tuesday, August 23, 2016

Project Deadline Extended Reason: So many great designs coming in that I wanted a few extra days to tweek!Great job all Added Friday, August 26, 2016

Project Deadline Extended Reason: Very good designs thus far. We just need a few more days.Thanks Added Wednesday, August 31, 2016

Target Market(s)

High end grocery and specialty stores.

Our side panel on the label will say "At Lumora we're fanatics for great flavors and are passionate about finding the best ingredients. From simple to elegant our products are "simply lumora".

Industry/Entity Type

It Company

Font styles to use
Serif
Decorative
Script

Requirements
Must have
• A label that will draw the consumer to pick it up! Need something bold and elegant...
Nice to have
• Again, I really would like to have a label that pops. Since the bottle front is only about 2inches in width it will need some creativity. Would like something very simple and elegant.
• If the designer does not like the logo, please feel free to design without it!
Should not have
• Dark dark colors. We are selling dressing and we don't want any colors that may distort the contents.
• No stock photos for the front. I don't want our dressing to look like the others on the self. Brackwell Pantry just uses lettering and a their packaging is eye catching

```html
<!DOCTYPE html>
<html lang="en">
<head>
<meta charset="utf-8">
<title>Lumora White Balsmic Vinaigrette – Label Options</title>
<link href="https://fonts.googleapis.com/css2?family=Cinzel:wght@400;500&family=Cormorant+SC:wght@400;500&family=Montserrat:wght@400&display=swap" rel="stylesheet">
<style>
  :root {
    --page: #ffffff;
    --forest: #022b0f;
    --wine: #850b17;
    --silver-light: #f1f1f1;
    --silver-mid: #c9c9cb;
    --gold: #e2bb1c;
    --ink-light: #ffffff;
    --ink-silver: #7d7d80;
    --caption: #333333;
  }
  * { margin: 0; padding: 0; box-sizing: border-box; }
  html, body { width: 1200px; height: 1200px; overflow: hidden; background: var(--page); }
  .canvas { position: relative; width: 1200px; height: 1200px; }

  .label-front, .label-side {
    position: absolute;
    width: 124px; height: 310px;
    border-radius: 4px 8px 8px 4px;
    overflow: hidden;
  }
  .label-side { width: 64px; border-radius: 9px; }

  .variant-forest { background: var(--forest); color: var(--ink-light); }
  .variant-wine { background: var(--wine); color: var(--ink-light); }
  .variant-silver {
    background: linear-gradient(90deg, var(--silver-mid) 0%, var(--silver-light) 35%, #ffffff 55%, var(--silver-mid) 100%);
    color: var(--ink-silver);
  }

  .drop { position: absolute; left: 50%; top: 0; transform: translateX(-50%); width: 22px; height: 170px; }

  .brand {
    position: absolute; top: 214px; left: 0; right: 0; text-align: center;
    font-family: "Cinzel", serif; font-size: 11px; color: var(--gold); line-height: 1;
  }
  .brand-tag {
    position: absolute; top: 227px; left: 0; right: 0; text-align: center;
    font-family: "Montserrat", sans-serif; font-size: 2.6px; color: var(--gold); letter-spacing: .3px; text-transform: uppercase;
  }
  .product-name {
    position: absolute; top: 233px; left: 0; right: 0; text-align: center;
    font-family: "Cinzel", serif; font-size: 19px; line-height: 17px; letter-spacing: .4px;
  }
  .product-type {
    position: absolute; top: 270px; left: 0; right: 0; text-align: center;
    font-family: "Cormorant SC", serif; font-size: 8px; letter-spacing: .6px;
  }
  .volume {
    position: absolute; top: 287px; left: 0; right: 0; text-align: center;
    font-family: "Cormorant SC", serif; font-size: 6px;
  }

  .side-copy {
    position: absolute; left: 50%; top: 50%;
    width: 280px;
    transform: translate(-50%, -50%) rotate(-90deg);
    font-family: "Cormorant SC", serif; font-size: 6.2px; line-height: 15px; letter-spacing: .3px;
  }
  .side-copy p { white-space: nowrap; }

  .finish-caption {
    position: absolute; font-family: "Montserrat", sans-serif; font-size: 15px; color: var(--caption); letter-spacing: .2px;
  }
  .finish-swatch { position: absolute; width: 182px; height: 265px; }
  .finish-foil-green { background: radial-gradient(circle at 75% 45%, #5c7a2c 0%, #2c5a1e 40%, #214a16 100%); }
  .finish-foil-red { background: linear-gradient(160deg, #b3141c 0%, #8f0c14 60%, #e8a11c 100%); }
  .finish-foil-metal { background: linear-gradient(135deg, #e6e6e6 0%, #8a8a8a 45%, #d6b829 70%, #4a4a4a 100%); }
</style>
</head>
<body>
<main class="canvas">

  <!-- Forest green option -->
  <section class="label-front variant-forest" style="left:68px; top:228px;">
    <svg class="drop" viewBox="0 0 22 170" aria-hidden="true">
      <line x1="11" y1="0" x2="11" y2="136" stroke="#e2bb1c" stroke-width="1.6"/>
      <path d="M11 132 C13 142 21 149 21 158 A10 10 0 0 1 1 158 C1 149 9 142 11 132 Z" fill="#e2bb1c"/>
    </svg>
    <div class="brand">Lumora</div>
    <div class="brand-tag">naturally gourmet dressings</div>
    <h2 class="product-name">WHITE<br>BALSMIC</h2>
    <div class="product-type">Vinaigrette</div>
    <div class="volume">250 ml</div>
  </section>
  <section class="label-side variant-forest" style="left:236px; top:228px;">
    <div class="side-copy">
      <p>At Lumora we're fanatics for great flavors and are passionate</p>
      <p>&nbsp;&nbsp;&nbsp;&nbsp;about finding&nbsp;&nbsp;the best ingredients.</p>
      <p>From simple to elegant our products are "simply lumora"</p>
    </div>
  </section>
  <div class="finish-caption" style="left:373px; top:145px;">Finishing Example</div>
  <div class="finish-swatch finish-foil-green" style="left:373px; top:177px;" role="img" aria-label="Finishing sample: gold foil emblem stamped on green textured paper"></div>

  <!-- Wine red option -->
  <section class="label-front variant-wine" style="left:665px; top:228px;">
    <svg class="drop" viewBox="0 0 22 170" aria-hidden="true">
      <line x1="11" y1="0" x2="11" y2="136" stroke="#e2bb1c" stroke-width="1.6"/>
      <path d="M11 132 C13 142 21 149 21 158 A10 10 0 0 1 1 158 C1 149 9 142 11 132 Z" fill="#e2bb1c"/>
    </svg>
    <div class="brand">Lumora</div>
    <div class="brand-tag">naturally gourmet dressings</div>
    <h2 class="product-name">WHITE<br>BALSMIC</h2>
    <div class="product-type">Vinaigrette</div>
    <div class="volume">250 ml</div>
  </section>
  <section class="label-side variant-wine" style="left:835px; top:228px;">
    <div class="side-copy">
      <p>At Lumora we're fanatics for great flavors and are passionate</p>
      <p>&nbsp;&nbsp;&nbsp;&nbsp;about finding&nbsp;&nbsp;the best ingredients.</p>
      <p>From simple to elegant our products are "simply lumora"</p>
    </div>
  </section>
  <div class="finish-caption" style="left:962px; top:145px;">Finishing Example</div>
  <div class="finish-swatch finish-foil-red" style="left:962px; top:177px;" role="img" aria-label="Finishing sample: red label with gold foil panel and embossed lettering"></div>

  <!-- Silver option -->
  <section class="label-front variant-silver" style="left:390px; top:795px;">
    <svg class="drop" viewBox="0 0 22 170" aria-hidden="true">
      <line x1="11" y1="0" x2="11" y2="136" stroke="#e2bb1c" stroke-width="1.6"/>
      <path d="M11 132 C13 142 21 149 21 158 A10 10 0 0 1 1 158 C1 149 9 142 11 132 Z" fill="#e2bb1c"/>
    </svg>
    <div class="brand">Lumora</div>
    <div class="brand-tag">naturally gourmet dressings</div>
    <h2 class="product-name">WHITE<br>BALSMIC</h2>
    <div class="product-type">Vinaigrette</div>
    <div class="volume">250 ml</div>
  </section>
  <section class="label-side variant-silver" style="left:560px; top:795px;">
    <div class="side-copy">
      <p>At Lumora we're fanatics for great flavors and are passionate</p>
      <p>&nbsp;&nbsp;&nbsp;&nbsp;about finding&nbsp;&nbsp;the best ingredients.</p>
      <p>From simple to elegant our products are "simply lumora"</p>
    </div>
  </section>
  <div class="finish-caption" style="left:718px; top:721px;">Finishing Example</div>
  <div class="finish-swatch finish-foil-metal" style="left:718px; top:754px;" role="img" aria-label="Finishing sample: metallic silver pouch with bold gold print"></div>

</main>
</body>
</html>
```